Lantern Marketing Group (LMG)

This is for my business cards. I want a Nice anfd Elegant Business Card to be Designed, Using more or less of the same colors of my logo that i have attached.i would like to have these business cards forever

Thank you

Thank you

Thank you

Contact Information for Business Card

Tobias Rennard
Lantern Marketing Group
C.(555) 214-6083
E-Mail. TRennard@lanternmgroup.example

Font styles to use
Serif
Sans Serif

Colors
d0dfed
cbcbcb
cee9f5

Requirements
Must have
• (LMG)
• Lantern Marketing Group
Nice to have
• 3D affects
Should not have
• Please try not using the flat version of the logo try and use the 3d version please

```html
<!DOCTYPE html>
<html lang="en">
<head>
<meta charset="utf-8">
<title>Lantern Marketing Group — Business Card</title>
<link rel="stylesheet" href="https://fonts.googleapis.com/css2?family=Lato:wght@400;700;900&display=swap">
<style>
  :root {
    --stage: #1b1b1d;
    --card-white: #f7f8f9;
    --card-shade: #e6e8ea;
    --brand-blue: #2b8fd4;
    --brand-blue-deep: #1c6fb6;
    --brand-blue-light: #4aa6e3;
    --ink: #1a1a1a;
    --ink-soft: #3a3a3a;
    --rule: #9fb7cc;
    --white: #ffffff;
  }
  * { box-sizing: border-box; margin: 0; padding: 0; }
  html, body {
    width: 1200px; height: 864px; overflow: hidden;
    background: var(--stage);
    font-family: "Lato", Arial, sans-serif;
  }
  .sheet {
    width: 1200px; height: 864px;
    display: flex; align-items: center; justify-content: center; gap: 40px;
  }
  .card {
    position: relative;
    width: 540px; height: 309px;
    overflow: hidden;
    box-shadow: 0 14px 30px rgba(0,0,0,.55);
  }

  /* Front */
  .card--front {
    background: linear-gradient(135deg, var(--white) 0%, var(--card-white) 55%, var(--card-shade) 100%);
  }
  .edge-tab {
    position: absolute; width: 12px;
    background: linear-gradient(180deg, var(--brand-blue-light), var(--brand-blue-deep));
  }
  .edge-tab--left { left: 0; top: 0; height: 62%; border-radius: 0 6px 6px 0; }
  .edge-tab--right { right: 0; top: 36%; height: 64%; border-radius: 6px 0 0 6px; }
  .contact {
    position: absolute; left: 52px; top: 88px;
  }
  .contact__name {
    font-weight: 900; font-size: 17px; letter-spacing: .4px;
    color: var(--ink); text-transform: uppercase;
  }
  .contact__company {
    margin-top: 2px;
    font-size: 12.5px; color: var(--brand-blue); text-transform: uppercase; letter-spacing: .3px;
  }
  .contact__list { list-style: none; margin-top: 14px; }
  .contact__item {
    display: flex; align-items: center; gap: 8px;
    font-size: 12.5px; color: var(--ink-soft); margin-bottom: 6px;
  }
  .contact__icon { width: 12px; height: 12px; fill: var(--brand-blue-deep); flex: none; }
  .divider {
    position: absolute; left: 300px; top: 92px; width: 1px; height: 112px;
    background: var(--rule);
  }
  .brand-mark {
    position: absolute; left: 300px; right: 12px; top: 0; bottom: 0;
    display: flex; align-items: center; justify-content: center; gap: 12px;
  }
  .brand-mark__square {
    width: 22px; height: 22px; background: var(--brand-blue);
  }
  .brand-mark__text {
    font-weight: 900; font-size: 64px; letter-spacing: 2px; color: var(--brand-blue);
  }

  /* Back */
  .card--back {
    background: linear-gradient(150deg, var(--brand-blue-light) 0%, var(--brand-blue) 45%, var(--brand-blue-deep) 100%);
    display: flex; flex-direction: column; align-items: center; justify-content: center;
    color: var(--white);
  }
  .back-brand__initials {
    font-weight: 900; font-size: 56px; letter-spacing: 3px; line-height: 1;
  }
  .back-brand__name {
    margin-top: 12px;
    font-weight: 900; font-size: 30px; letter-spacing: 2px; text-transform: uppercase; line-height: 1;
  }
  .back-brand__tagline {
    margin-top: 8px;
    font-weight: 900; font-size: 15px; letter-spacing: 4px; text-transform: uppercase;
  }
</style>
</head>
<body>
<main class="sheet">
  <section class="card card--front" aria-label="Business card front">
    <span class="edge-tab edge-tab--left"></span>
    <span class="edge-tab edge-tab--right"></span>
    <div class="contact">
      <h1 class="contact__name">Tobias Rennard</h1>
      <p class="contact__company">Lantern Marketing Group</p>
      <ul class="contact__list">
        <li class="contact__item">
          <svg class="contact__icon" viewBox="0 0 24 24" aria-hidden="true"><path d="M6.6 10.8a15.1 15.1 0 0 0 6.6 6.6l2.2-2.2a1 1 0 0 1 1-.25 11.4 11.4 0 0 0 3.6.57 1 1 0 0 1 1 1V20a1 1 0 0 1-1 1A17 17 0 0 1 3 4a1 1 0 0 1 1-1h3.5a1 1 0 0 1 1 1c0 1.25.2 2.45.57 3.57a1 1 0 0 1-.25 1z"/></svg>
          <span>(555) 214-6083</span>
        </li>
        <li class="contact__item">
          <svg class="contact__icon" viewBox="0 0 24 24" aria-hidden="true"><path d="M2 5h20v14H2z M3.5 6.5 12 13l8.5-6.5" fill="none" stroke="currentColor"/><path d="M2 5h20v14H2zm2 2v.3l8 5.6 8-5.6V7z"/></svg>
          <span>TRennard@lanternmgroup.example</span>
        </li>
      </ul>
    </div>
    <span class="divider"></span>
    <div class="brand-mark">
      <span class="brand-mark__square"></span>
      <span class="brand-mark__text">LMG</span>
    </div>
  </section>

  <section class="card card--back" aria-label="Business card back">
    <p class="back-brand__initials">LMG</p>
    <p class="back-brand__name">Lantern</p>
    <p class="back-brand__tagline">Marketing Group</p>
  </section>
</main>
</body>
</html>
```